Letterhead Design for Law Firm that Specializes in Property Damage Litigation

We are looking for a redesign of our letterhead. Our current letterhead lists all of our current staff members and we'd like to come up with a design that does NOT list all of the staff members so that it does not need to be updated with every newly hired employee. Must be in editable format.

We are a law firm that specializes in property damage, so we need something that is professional, yet modern. The final design should use our existing logo and should use a blue color scheme (alternate colors would be gray, black, and white).

Industry/Entity Type

Legal

Colors
0054AA
0677BA
7BADD7
CADEEF
E8F1F8

```html
<!DOCTYPE html>
<html lang="en">
<head>
<meta charset="utf-8">
<title>Hartwell Morrow &amp; Caine – Letterhead</title>
<link rel="stylesheet" href="https://fonts.googleapis.com/css2?family=Roboto:wght@400;500;700&display=swap">
<style>
  :root {
    --paper: #e0e0e0;
    --paper-shade: #d6d6d6;
    --navy: #1d3768;
    --text-grey: #5f6266;
    --rule: #6b6d70;
  }
  html, body {
    margin: 0;
    padding: 0;
    width: 1023px;
    height: 1200px;
    overflow: hidden;
  }
  .letterhead {
    position: relative;
    width: 1023px;
    height: 1200px;
    background: linear-gradient(90deg, #e6e6e6 0%, var(--paper) 30%, var(--paper-shade) 100%);
    font-family: "Roboto", Arial, sans-serif;
    color: var(--text-grey);
  }
  .brand {
    position: absolute;
    left: 94px;
    top: 78px;
    width: 260px;
  }
  .brand-name {
    display: flex;
    align-items: center;
    gap: 10px;
    margin: 0;
    font-size: 24px;
    font-weight: 500;
    line-height: 1.1;
    color: var(--navy);
  }
  .brand-mark {
    flex: none;
    width: 16px;
    height: 16px;
    background: var(--navy);
  }
  .brand-tagline {
    margin: 14px 0 0;
    font-size: 10px;
    font-weight: 500;
    letter-spacing: 2.2px;
    text-transform: uppercase;
    color: var(--text-grey);
  }
  .office {
    position: absolute;
    top: 80px;
    font-size: 15px;
    line-height: 19px;
  }
  .office--pa { left: 440px; }
  .office--nj { left: 716px; }
  .office-title {
    margin: 0 0 2px;
    font-size: 14px;
    font-weight: 500;
    text-transform: uppercase;
    color: var(--navy);
  }
  .office address {
    font-style: normal;
  }
  .office-phone {
    margin: 4px 0 0;
    font-size: 16px;
    font-weight: 500;
    color: var(--navy);
  }
  .office-divider {
    position: absolute;
    left: 653px;
    top: 80px;
    width: 1px;
    height: 98px;
    background: var(--rule);
  }
  .footer {
    position: absolute;
    left: 100px;
    right: 83px;
    top: 1124px;
    display: flex;
    align-items: center;
    gap: 8px;
  }
  .footer-rule {
    flex: 1;
    height: 1px;
    background: var(--rule);
  }
  .footer-web {
    font-size: 14px;
    letter-spacing: 3px;
    color: var(--text-grey);
  }
  .footer-web strong {
    font-weight: 700;
    color: var(--navy);
  }
</style>
</head>
<body>
  <main class="letterhead">
    <header>
      <div class="brand">
        <h1 class="brand-name"><span class="brand-mark"></span>Hartwell Morrow &amp; Caine</h1>
        <p class="brand-tagline">The Property Damage Attorneys</p>
      </div>

      <section class="office office--pa">
        <h2 class="office-title">Philadelphia</h2>
        <address>2450 Market Street<br>Suite 840<br>Philadelphia, PA 19103</address>
        <p class="office-phone">215.555.0140</p>
      </section>

      <div class="office-divider"></div>

      <section class="office office--nj">
        <h2 class="office-title">New Jersey</h2>
        <address>318 Haddon Avenue<br>Suite 110<br>Cherry Hill, NJ 08034</address>
        <p class="office-phone">856.555.0172</p>
      </section>
    </header>

    <footer class="footer">
      <span class="footer-rule"></span>
      <span class="footer-web">www.<strong>hmclegal</strong>.com</span>
      <span class="footer-rule"></span>
    </footer>
  </main>
</body>
</html>
```